R. Talbin Group Business Card

We are looking for a business card mock-up.

Contact Information for Business Card

This is the information that needs to be included:
Name
Title
The R. Talbin Group Inc. Insurance Agents & Brokers (needs to be listed out in entirety)
Logo
License 0482316 (needs to be same sized font as phone number)
Address (728 North Vale Avenue, Los Angeles, CA 90047)
Telephone number ( 714-389-2076 ext. 131)Fax number (714-389-4152)
Email
Website (www.rtalbinagency.example)
Cities (Anaheim, Los Angeles, San Jose, Torrance)

```html
<!DOCTYPE html>
<html lang="en">
<head>
<meta charset="utf-8">
<title>R. Talbin Group Business Card</title>
<link rel="stylesheet" href="https://fonts.googleapis.com/css2?family=Tinos:wght@400;700&display=swap">
<style>
  :root{
    --bg:#2b2b2b;
    --card:#ffffff;
    --ink:#1e1e1e;
    --copper:#b5763f;
    --band:#2a2a2a;
    --band-text:#f2f2f2;
    --muted:#555555;
  }
  *{box-sizing:border-box;margin:0;padding:0}
  html,body{width:1200px;height:903px;overflow:hidden;background:var(--bg)}
  body{font-family:"Tinos","Times New Roman",serif;color:var(--ink);position:relative}
  .card{position:absolute;width:560px;height:320px;background:var(--card);box-shadow:0 10px 30px rgba(0,0,0,.5);overflow:hidden}
  .card-front{left:60px;top:70px}
  .card-back{left:580px;top:470px}

  .brand{display:flex;align-items:center;gap:12px}
  .brand-mark{width:52px;height:52px;border-radius:50%;background:var(--copper);flex:none}
  .brand-name{font-size:34px;letter-spacing:2px;color:var(--ink);line-height:1;white-space:nowrap}
  .brand-sub{font-size:9px;letter-spacing:6px;color:var(--ink);margin-top:4px}

  .card-front .brand{position:absolute;left:50%;top:112px;transform:translateX(-50%)}
  .stay{position:absolute;right:70px;bottom:62px;display:flex;align-items:center;gap:8px;font-size:12px}
  .stay .dot{width:10px;height:10px;border-radius:50%;background:var(--copper)}

  .card-back .brand{position:absolute;right:30px;top:30px}
  .card-back .brand-mark{width:46px;height:46px}
  .card-back .brand-name{font-size:30px}
  .tagline{font-size:8.5px;letter-spacing:2px;border-top:1px solid var(--ink);padding-top:2px;margin-top:3px}

  .name-tag{position:absolute;left:0;top:96px;display:flex;height:56px}
  .name-tag .edge{width:40px;background:#444}
  .name-tag .gap{width:6px}
  .name-tag .label{background:var(--copper);color:#fff;padding:8px 26px 0 20px;width:320px}
  .person{font-size:22px;letter-spacing:.5px}
  .role{font-size:13px}

  .contact{position:absolute;left:88px;top:178px;list-style:none}
  .contact li{display:flex;align-items:center;gap:10px;font-size:15px;height:22px}
  .contact svg{width:16px;height:16px;flex:none}

  .office{position:absolute;right:34px;top:126px;text-align:right;font-size:14px;line-height:18px}
  .office .license{color:var(--copper)}

  .cities{position:absolute;left:0;right:0;bottom:0;height:48px;background:var(--band);color:var(--band-text);display:flex;align-items:center;justify-content:center;gap:8px;font-size:16px}
  .cities .sep{width:5px;height:5px;border-radius:50%;background:var(--copper)}
</style>
</head>
<body>
  <section class="card card-front">
    <div class="brand">
      <span class="brand-mark"></span>
      <div>
        <div class="brand-name">R TALBIN CO</div>
        <div class="brand-sub">INCORPORATED</div>
      </div>
    </div>
    <div class="stay">
      <span>Stay Connected :</span>
      <span class="dot"></span><span class="dot"></span><span class="dot"></span><span class="dot"></span>
    </div>
  </section>

  <section class="card card-back">
    <div class="brand">
      <span class="brand-mark"></span>
      <div>
        <div class="brand-name">R TALBIN CO</div>
        <div class="brand-sub">INCORPORATED</div>
        <div class="tagline">INSURANCE AGENTS &amp; BROKERS</div>
      </div>
    </div>

    <div class="name-tag">
      <span class="edge"></span><span class="gap"></span>
      <div class="label">
        <div class="person">Dorian Whitcombe</div>
        <div class="role">Managing Director</div>
      </div>
    </div>

    <ul class="contact">
      <li><svg viewBox="0 0 16 16"><circle cx="8" cy="8" r="8" fill="#b5763f"/><path d="M5 4l2 2-1 1c.5 1.2 1.8 2.5 3 3l1-1 2 2-1.5 1.5C7.5 12 4 8.5 3.5 5.5z" fill="#fff"/></svg>714-389-2076 ext. 131</li>
      <li><svg viewBox="0 0 16 16"><circle cx="8" cy="8" r="8" fill="#b5763f"/><rect x="5" y="4" width="6" height="3" fill="#fff"/><rect x="4" y="7" width="8" height="4" fill="#fff"/><rect x="5.5" y="9.5" width="5" height="2.5" fill="#b5763f" stroke="#fff" stroke-width=".8"/></svg>714.389.4152</li>
      <li><svg viewBox="0 0 16 16"><circle cx="8" cy="8" r="8" fill="#b5763f"/><rect x="4" y="5" width="8" height="6" fill="none" stroke="#fff"/><path d="M4 5l4 3.5L12 5" fill="none" stroke="#fff"/></svg>info@rtalbinagency.example</li>
      <li><svg viewBox="0 0 16 16"><circle cx="8" cy="8" r="8" fill="#b5763f"/><circle cx="8" cy="8" r="4.5" fill="none" stroke="#fff"/><path d="M3.5 8h9M8 3.5v9" stroke="#fff"/></svg>www.rtalbinagency.example</li>
    </ul>

    <div class="office">
      <div class="license">CA License# 0482316</div>
      <div>The R. Talbin Group, Inc</div>
      <div>728 North Vale Avenue, Ste. 100</div>
      <div>Los Angeles, CA 90047</div>
    </div>

    <div class="cities">
      <span>Cities :</span><span>Anaheim</span><span class="sep"></span><span>Los Angeles</span><span class="sep"></span><span>San Jose</span><span class="sep"></span><span>Torrance</span>
    </div>
  </section>
</body>
</html>
```